Magazine Ad for the Waste Industry

We need a full page ad design that will help us introduce our new engine cooling system into the Waste market. This system helps regulate engine temperatures for large trash trucks with its advanced technology and durable. We would like this ad to make an impact and stand out from the more cluttered looking ads that are seen in trade magazines.
The project must be submitted in either InDesign or Photoshop files.

Target Market(s)

Waste Industry, Trash truck manufacturers

Industry/Entity Type

Waste Management

Font styles to use
Sans Serif

Colors
0255a3

Requirements
Must have
• The text and images attached with a more modern industrial/masculine feel.
• Our Company colors are...
• Blue (RGB 25, 76, 159)
• Gray (RGB 129, 130, 133)
• White and black as accents as needed
• SIZING
• Spread Bleed: 9.5" x 11.375"
Nice to have
• I attached two files for a font that we have used in the past. Another font we use commonly is Ariel.

```html
<!DOCTYPE html>
<html lang="en">
<head>
<meta charset="utf-8">
<title>Advanced Electric Engine Cooling – Kelvar</title>
<link href="https://fonts.googleapis.com/css2?family=Exo+2:ital,wght@0,400;0,500;0,800;1,800&display=swap" rel="stylesheet">
<style>
  :root {
    --brand-blue: #194c9f;
    --brand-blue-deep: #0f3a85;
    --brand-blue-bright: #0255a3;
    --brand-gray: #818285;
    --ring-light: #e4e8f0;
    --ring-mid: #cfd6e4;
    --paper: #ffffff;
    --stage: #d9d9d9;
    --hardware-dark: #26282b;
    --hardware-mid: #4a4d52;
  }
  html, body {
    margin: 0;
    width: 1200px;
    height: 900px;
    overflow: hidden;
    background: var(--stage);
    font-family: "Exo 2", Arial, sans-serif;
  }
  .ad-page {
    position: absolute;
    left: 241px;
    top: 20px;
    width: 718px;
    height: 860px;
    background: var(--paper);
    overflow: hidden;
    box-shadow: 0 4px 18px rgba(0,0,0,.18);
  }
  .ad-backdrop {
    position: absolute;
    inset: 0;
  }
  .headline {
    position: absolute;
    top: 58px;
    left: 0;
    width: 100%;
    margin: 0;
    text-align: center;
    color: var(--brand-blue);
    font-weight: 800;
    font-style: italic;
    font-size: 54px;
    line-height: 1.05;
    letter-spacing: 1px;
  }
  .product-shot {
    position: absolute;
    left: 300px;
    top: 210px;
    width: 280px;
    height: 270px;
    background: linear-gradient(135deg, var(--hardware-mid), var(--hardware-dark));
    transform: rotate(-4deg);
    box-shadow: 0 6px 14px rgba(0,0,0,.3);
  }
  .series-mark {
    position: absolute;
    left: 118px;
    top: 400px;
    display: flex;
    align-items: center;
    gap: 8px;
    color: var(--brand-gray);
    font-weight: 800;
    font-size: 22px;
  }
  .series-mark .dot {
    width: 30px;
    height: 30px;
    border-radius: 50%;
    background: var(--brand-gray);
  }
  .benefits {
    position: absolute;
    left: 78px;
    top: 555px;
    margin: 0;
    padding: 0;
    list-style: none;
    color: var(--paper);
    font-weight: 500;
    font-size: 25px;
    line-height: 44px;
  }
  .benefits li {
    display: flex;
    align-items: center;
    gap: 12px;
  }
  .benefits li::before {
    content: "";
    width: 11px;
    height: 11px;
    border-radius: 50%;
    background: var(--paper);
    box-shadow: 0 0 0 3px var(--brand-blue), 0 0 0 5px var(--paper);
    margin: 0 6px 0 6px;
  }
  .company-name {
    position: absolute;
    right: 52px;
    top: 640px;
    color: var(--paper);
    font-weight: 800;
    font-size: 64px;
    letter-spacing: 1px;
  }
  .web-address {
    position: absolute;
    left: 78px;
    bottom: 26px;
    color: var(--brand-blue);
    font-size: 15px;
    letter-spacing: 1px;
  }
</style>
</head>
<body>
  <article class="ad-page">
    <svg class="ad-backdrop" width="718" height="860" viewBox="0 0 718 860" aria-hidden="true">
      <defs>
        <linearGradient id="panel-fill" x1="0" y1="0" x2="1" y2="1">
          <stop offset="0" stop-color="#1d5bb8"/>
          <stop offset="1" stop-color="#0f3a85"/>
        </linearGradient>
        <clipPath id="panel-clip"><rect x="40" y="490" width="678" height="305"/></clipPath>
      </defs>
      <g class="target-rings">
        <circle cx="360" cy="450" r="290" fill="#f1f3f7"/>
        <circle cx="360" cy="450" r="215" fill="var(--ring-light)"/>
        <circle cx="360" cy="450" r="140" fill="var(--ring-mid)"/>
      </g>
      <rect class="info-panel" x="40" y="490" width="678" height="305" fill="url(#panel-fill)"/>
      <g clip-path="url(#panel-clip)" fill="#ffffff">
        <circle cx="360" cy="450" r="290" opacity=".06"/>
        <circle cx="360" cy="450" r="215" opacity=".08"/>
        <circle cx="360" cy="450" r="140" opacity=".1"/>
      </g>
      <circle cx="360" cy="450" r="62" fill="var(--brand-blue-bright)"/>
      <circle cx="360" cy="450" r="36" fill="#ffffff"/>
    </svg>

    <h1 class="headline">Advanced Electric<br>Engine Cooling</h1>

    <div class="product-shot" role="img" aria-label="Black electric engine cooling module with four reversible fans"></div>

    <div class="series-mark"><span class="dot"></span>Eco-Blend</div>

    <ul class="benefits">
      <li>Fully Reversible Fans</li>
      <li>Eliminate Preventative Maintenance</li>
      <li>Average 8% Fuel Economy</li>
      <li>Increase Horsepower</li>
      <li>Quieter Residential Operation</li>
    </ul>

    <div class="company-name">Kelvar</div>

    <div class="web-address">www.kelvar-corp.com/refuse</div>
  </article>
</body>
</html>
```